New Fun, Positive, energised looking Business Card Needed for High Achiever Coach

I am looking for a two sided full colour business card. I am self employed and have recently re branded my 1-2-1 work re-vitalising high achievers. My target client base for these cards is therefore high achievers - usually aged 40 -55, they are often entrepreneurs, CEO or work in banking and finance and 2/3 are male. I work with them on 90 day or 6 month coaching programs to help them live their success in a healthier, more sustainable and fulfiiled way. They pay for this privately so though they are corporate types the cards need not look 'corporate'. I want to portray the idea of transformation, vitality and re-connecting.
You can get a feel for the look I like on my new website: corinvale.co.uk
I want to use this logo with strapline (Re-Vitalising High Achievers) (I purchased off Logoharbor) and font/ colours (the turquoise and green).
Details to include on the card:
www.corinvale.co.uk
+44 7915 264318
mira@corinvale.co.uk
skype: miracorin
I'd also like to include:
Do you struggle to switch off? Want to be healthier and feel fitter? Want closer relationships? More clarity over the direction you are headed? I can help you do these things using integrated mind-body techniques. Visit corinvale.co.uk TODAY to apply for a FREE Breakthrough session.
BUT if that is too much text for a card I am open to advice/ammendments.
Updates
Thanks for your design - I am considering them. PLease change the wording to :

```html
<!DOCTYPE html>
<html lang="en">
<head>
<meta charset="utf-8">
<title>Mira Corin – Business Card</title>
<link rel="stylesheet" href="https://fonts.googleapis.com/css2?family=Arvo:wght@400;700&family=Alfa+Slab+One&family=Dancing+Script:wght@400;500&display=swap">
<style>
  :root {
    --backdrop: #2b2b2b;
    --turquoise: #1b97c1;
    --turquoise-light: #33b0d6;
    --turquoise-deep: #1590b9;
    --leaf-green: #5aa55a;
    --paper: #f0f0ef;
    --white: #ffffff;
    --question-tint: rgba(215, 240, 248, 0.72);
  }
  * { box-sizing: border-box; margin: 0; padding: 0; }
  html, body {
    width: 1200px;
    height: 896px;
    overflow: hidden;
    background: var(--backdrop);
  }
  .canvas {
    position: relative;
    width: 1200px;
    height: 896px;
  }
  .card {
    position: absolute;
    left: 353px;
    width: 485px;
    height: 268px;
    overflow: hidden;
  }

  /* Front: message side */
  .card--message {
    top: 165px;
    background: linear-gradient(160deg, var(--turquoise-light) 0%, var(--turquoise) 55%, var(--turquoise-deep) 100%);
    color: var(--white);
  }
  .corner {
    position: absolute;
    width: 36px;
    height: 36px;
    border-color: rgba(255, 255, 255, 0.9);
    border-style: solid;
    border-width: 0;
  }
  .corner--top-left { left: 29px; top: 21px; border-top-width: 1.5px; border-left-width: 1.5px; }
  .corner--bottom-right { left: 420px; top: 112px; border-bottom-width: 1.5px; border-right-width: 1.5px; }
  .questions {
    position: absolute;
    left: 0;
    top: 26px;
    width: 485px;
    text-align: center;
    font-family: "Dancing Script", cursive;
    font-size: 26px;
    line-height: 36.5px;
    color: var(--question-tint);
    list-style: none;
  }
  .pitch {
    position: absolute;
    left: 0;
    top: 155px;
    width: 485px;
    text-align: center;
    font-family: "Arvo", serif;
    font-size: 17.5px;
    line-height: 23.5px;
  }
  .pitch .site { text-decoration: underline; text-underline-offset: 3px; text-decoration-thickness: 1px; }
  .pitch strong { font-weight: 700; }

  /* Back: identity side */
  .card--identity {
    top: 473px;
    background: var(--paper);
    color: var(--turquoise);
  }
  .brand-dot {
    position: absolute;
    left: 36px;
    top: 46px;
    width: 46px;
    height: 46px;
    border-radius: 50%;
    background: var(--leaf-green);
  }
  .brand-name {
    position: absolute;
    left: 110px;
    top: 34px;
    font-family: "Alfa Slab One", serif;
    font-weight: 400;
    font-size: 39px;
    line-height: 48px;
    color: var(--turquoise);
  }
  .strapline {
    position: absolute;
    left: 111px;
    top: 84px;
    font-family: "Dancing Script", cursive;
    font-size: 23px;
    color: var(--turquoise);
  }
  .contact {
    position: absolute;
    top: 198px;
    font-family: "Arvo", serif;
    font-size: 13px;
    line-height: 18px;
    display: grid;
    column-gap: 0;
  }
  .contact--left { left: 34px; grid-template-columns: 63px auto; }
  .contact--right { left: 299px; grid-template-columns: 63px auto; }
  .contact dt { text-transform: uppercase; }
  .contact dd.web { grid-column: 1 / span 2; }
  .divider {
    position: absolute;
    left: 273px;
    top: 200px;
    width: 1.5px;
    height: 29px;
    background: var(--leaf-green);
  }
  .footer-band {
    position: absolute;
    left: 0;
    bottom: 0;
    width: 100%;
    height: 15px;
    background: var(--turquoise);
  }
</style>
</head>
<body>
<main class="canvas">
  <section class="card card--message" aria-label="Card front">
    <span class="corner corner--top-left"></span>
    <span class="corner corner--bottom-right"></span>
    <ul class="questions">
      <li>Do you struggle to switch off?</li>
      <li>Want to be healthier and feel fitter?</li>
      <li>Want closer relationships?</li>
    </ul>
    <p class="pitch">
      I can help you do these things using integrated<br>
      mind-body techniques. Visit <span class="site">corinvale.co.uk</span><br>
      <strong>TODAY</strong> to apply for a <strong>FREE</strong><br>
      Breakthrough session.
    </p>
  </section>

  <section class="card card--identity" aria-label="Card back">
    <span class="brand-dot" aria-hidden="true"></span>
    <h1 class="brand-name">Mira Corin</h1>
    <p class="strapline">Re-Vitalising High Achievers</p>

    <dl class="contact contact--left">
      <dt>Phone</dt><dd>+44 7915 264318</dd>
      <dt>Email</dt><dd>mira@corinvale.co.uk</dd>
    </dl>
    <span class="divider"></span>
    <dl class="contact contact--right">
      <dt>Skype</dt><dd>miracorin</dd>
      <dd class="web">www.corinvale.co.uk</dd>
    </dl>
    <div class="footer-band"></div>
  </section>
</main>
</body>
</html>
```